Free UK Delivery Banner for website

We require a banner for a website which stated free delivery and then terms and conditions apply written at the bottom of it somewhere. Please visit the website as the banner must look correlated to the overall theme. the picture attached must also be edited to make it look slick. The FREE DELIVERY must be in a larger text and very visible. The terms & Conditions Apply should be in a really small text and the bottom corner of the banner. The banner must be 1900px X 960px

Target Market(s)

online website

Industry/Entity Type

fashion

Font styles to use
Serif
Sans Serif
Decorative
Script

Requirements
Must have
• Large free delivery and terms and conditions apply at the bottom
Nice to have
• make it look nice
Should not have
• Leave it to the designers

```html
<!DOCTYPE html>
<html lang="en">
<head>
<meta charset="utf-8">
<title>Maribelle – Free Delivery</title>
<link href="https://fonts.googleapis.com/css2?family=Cinzel:wght@400&family=Poppins:wght@400;500;900&family=Kaushan+Script&display=swap" rel="stylesheet">
<style>
  :root {
    --page-bg: #efe9df;
    --site-bg: #ffffff;
    --ink: #111111;
    --nav-ink: #2b2b2b;
    --rule: #d9d4cc;
    --peach-light: #fdf0dc;
    --peach: #f9dcb3;
    --peach-deep: #f3c990;
    --box-dark: #1a1a1a;
    --box-mid: #3a3a3a;
    --window: #fbe3c2;
  }
  * { margin: 0; padding: 0; box-sizing: border-box; }
  html, body { width: 1200px; height: 900px; overflow: hidden; }
  body { background: var(--page-bg); font-family: "Poppins", sans-serif; color: var(--ink); position: relative; }

  .site { position: absolute; left: 0; top: 104px; width: 1200px; height: 692px; background: var(--site-bg); }

  .site-header { position: absolute; left: 0; top: 0; width: 100%; height: 104px; border-bottom: 1px solid var(--rule); }
  .search { position: absolute; left: 77px; top: 36px; width: 279px; height: 30px; border-bottom: 1.5px solid var(--ink); }
  .search svg { position: absolute; left: 9px; top: 4px; }
  .brand-name { position: absolute; left: 0; width: 100%; top: 52px; text-align: center; font-family: "Cinzel", serif; font-size: 34px; letter-spacing: 1px; color: var(--ink); }
  .login { position: absolute; left: 936px; top: 36px; display: flex; align-items: center; gap: 6px; font-family: "Cinzel", serif; font-size: 13px; color: #444; }
  .cart { position: absolute; left: 1096px; top: 40px; display: flex; align-items: center; gap: 6px; font-size: 12px; }

  .main-nav { position: absolute; left: 0; top: 104px; width: 100%; height: 56px; border-bottom: 1px solid var(--rule); }
  .main-nav a { position: absolute; top: 19px; font-size: 13px; letter-spacing: .6px; color: var(--nav-ink); text-decoration: none; }

  .banner { position: absolute; left: 92px; top: 160px; width: 1015px; height: 514px; overflow: hidden; }
  .banner-photo { position: absolute; inset: 0; background:
      radial-gradient(ellipse at 80% 20%, var(--peach-light), transparent 60%),
      linear-gradient(100deg, var(--peach-light) 0%, var(--peach) 45%, var(--peach-deep) 100%); }
  .package-photo { position: absolute; inset: 0;
      clip-path: polygon(735px 112px, 1015px 148px, 1015px 514px, 631px 452px, 547px 312px);
      background: linear-gradient(150deg, var(--box-dark) 0%, var(--box-mid) 45%, #5a5a5a 60%, var(--box-dark) 100%); }

  .offer { position: absolute; left: 0; top: 0; width: 100%; height: 100%; }
  .truck { position: absolute; left: 146px; top: 198px; transform: rotate(-5deg); }
  .offer-free { position: absolute; left: 287px; top: 164px; font-weight: 900; font-size: 92px; line-height: 1; letter-spacing: -1px; transform: rotate(-4deg); transform-origin: left bottom; }
  .offer-delivery { position: absolute; left: 90px; top: 232px; font-family: "Kaushan Script", cursive; font-size: 136px; line-height: 1; transform: rotate(-6deg); transform-origin: left bottom; }
  .terms { position: absolute; left: 34px; top: 482px; font-size: 10px; letter-spacing: .2px; }
</style>
</head>
<body>
  <div class="site">
    <header class="site-header">
      <div class="search">
        <svg width="16" height="16" viewBox="0 0 16 16"><circle cx="6.5" cy="6.5" r="5" fill="none" stroke="#333" stroke-width="2"/><line x1="10.2" y1="10.2" x2="14.5" y2="14.5" stroke="#333" stroke-width="2.4" stroke-linecap="round"/></svg>
      </div>
      <div class="brand-name">Maribelle</div>
      <div class="login">
        <svg width="20" height="20" viewBox="0 0 20 20"><circle cx="10" cy="6" r="4.5" fill="#111"/><path d="M1 20c0-6 4-8 9-8s9 2 9 8z" fill="#111"/></svg>
        <span>LOGIN</span>
      </div>
      <div class="cart">
        <svg width="14" height="13" viewBox="0 0 14 13"><path d="M0 1h3l2 7h7l2-5H4.5" fill="none" stroke="#111" stroke-width="1.6"/><path d="M4 3h10l-2 5H5z" fill="#111"/><circle cx="6" cy="11" r="1.5" fill="#111"/><circle cx="11" cy="11" r="1.5" fill="#111"/></svg>
        <span>0</span>
      </div>
    </header>

    <nav class="main-nav">
      <a style="left:279px">New Arrivals</a>
      <a style="left:426px">Embroidered</a>
      <a style="left:576px">Printed</a>
      <a style="left:688px">Plain Dress</a>
      <a style="left:827px">Privacy Policy</a>
    </nav>

    <section class="banner">
      <div class="banner-photo" role="img" aria-label="Softly lit boutique interior with an embroidered cream dress and a shopping bag, warm peach tones"></div>
      <div class="package-photo" role="img" aria-label="Open black gift box with branded tissue-wrapped order and a thank-you card"></div>
      <div class="offer">
        <svg class="truck" width="124" height="62" viewBox="0 0 124 62" aria-hidden="true">
          <g fill="#111">
            <rect x="0" y="12" width="26" height="5" rx="2.5"/>
            <rect x="6" y="22" width="20" height="5" rx="2.5"/>
            <rect x="12" y="32" width="14" height="5" rx="2.5"/>
            <rect x="30" y="2" width="58" height="40" rx="3"/>
            <path d="M91 12 H107 Q110 12 112 15 L121 28 Q122 30 122 32 V44 H91 Z"/>
            <rect x="30" y="40" width="92" height="6" rx="2"/>
          </g>
          <path d="M96 17 H106 L114 29 H96 Z" fill="var(--window)"/>
          <circle cx="50" cy="50" r="10" fill="#111"/><circle cx="50" cy="50" r="4" fill="var(--window)"/>
          <circle cx="106" cy="50" r="10" fill="#111"/><circle cx="106" cy="50" r="4" fill="var(--window)"/>
        </svg>
        <div class="offer-free">FREE</div>
        <div class="offer-delivery">Delivery</div>
        <div class="terms">TERMS &amp; CONDITIONS APPLY</div>
      </div>
    </section>
  </div>
</body>
</html>
```